RW Talbrook LLC Business Card - Civil Engineering & Consulting Firm

We need a Business Card that is elegant, and masculine.  It is our Professional Civil Engineering & Consulting Company located in San Antonio TX (Not s construction or builder firm- no gears & no tool images please). We provide civil engineering services including  commercial site plans, grading and drainage plans, utility plans, hydraulics and hydrology, land planning, utility coordination, and other general civil engineering services related to commercial and residential development.
We have 2 existing Logos. We would like to convey reliability, strength, trustworthiness and attention to detail.  Blues and orange tones as per logo We are OK with the use of a darker blue in the mix.  We have 2 logo versions - Full Company Name Logo to go on the back of card, & Small Icon Logo for the front w/ personal Info.

Target Market(s)
Architects, Real Estate Developers, Other Strctural Engineers, Surveyers, General Contractors
Industry/Entity Type
Professional Civil Engineering
Contact Information for Business Card
Name, Position, Address, Cell & Office #, email, and company website
Font styles to use
Other font styles liked:
- Avian
Requirements
Should not have
- No Tools, No Gears, no Cranes, or Construction Equipment.

```html
<!DOCTYPE html>
<html lang="en">
<head>
<meta charset="utf-8">
<title>RW Talbrook LLC – Business Card</title>
<link href="https://fonts.googleapis.com/css2?family=Montserrat:wght@400;500;700;800&display=swap" rel="stylesheet">
<style>
  :root {
    --backdrop: #2b2e33;
    --card-dark: #38404b;
    --card-light: #f4f5f8;
    --brand-blue: #73a9d8;
    --brand-orange: #f0902a;
    --band-grey: #59606c;
    --text-light: #ffffff;
  }
  * { margin: 0; padding: 0; box-sizing: border-box; }
  html, body { width: 1200px; height: 1021px; overflow: hidden; }
  body {
    background: var(--backdrop);
    font-family: "Montserrat", sans-serif;
    position: relative;
  }
  .card {
    position: absolute;
    width: 580px;
    height: 332px;
    box-shadow: 0 18px 40px rgba(0,0,0,0.45);
  }
  /* Back of card: full company name */
  .card--back {
    left: 570px;
    top: 130px;
    background: var(--card-light);
    display: flex;
    align-items: center;
    justify-content: center;
    gap: 18px;
  }
  .wordmark {
    color: var(--brand-blue);
    font-weight: 500;
    letter-spacing: 0.08em;
    text-transform: uppercase;
    white-space: nowrap;
  }
  .card--back .wordmark { font-size: 38px; }
  .mark-square {
    width: 26px; height: 26px;
    background: var(--brand-orange);
    flex: none;
  }
  /* Front of card: personal info */
  .card--front {
    left: 50px;
    top: 560px;
    background: var(--card-dark);
    overflow: hidden;
  }
  .front-logo {
    position: absolute;
    left: 0; top: 0;
    width: 268px; height: 100%;
    display: flex; align-items: center; justify-content: center; gap: 9px;
  }
  .front-logo .wordmark { font-size: 15px; letter-spacing: 0.06em; }
  .front-logo .mark-square { width: 12px; height: 12px; }
  .divider-band {
    position: absolute;
    left: 268px; top: 0;
    width: 10px; height: 100%;
    background: var(--band-grey);
  }
  .contact-block {
    position: absolute;
    left: 318px; top: 36px;
    color: var(--text-light);
  }
  .person-name {
    color: var(--brand-orange);
    font-weight: 800;
    font-size: 27px;
    line-height: 1;
    white-space: nowrap;
  }
  .person-name .surname { text-transform: uppercase; }
  .person-role {
    color: var(--brand-blue);
    font-size: 11px;
    letter-spacing: 0.08em;
    margin-top: 3px;
  }
  .rule-pair { display: flex; gap: 6px; margin-top: 6px; }
  .rule-pair span { height: 2px; }
  .rule-white { width: 58px; background: var(--text-light); }
  .rule-orange { width: 140px; background: var(--brand-orange); }
  .contact-list { list-style: none; margin-top: 20px; }
  .contact-item {
    display: flex; align-items: center; gap: 14px;
    font-size: 13px; line-height: 1.3;
    margin-bottom: 14px;
  }
  .contact-icon { width: 26px; height: 26px; flex: none; }
</style>
</head>
<body>
  <section class="card card--back" aria-label="Business card back">
    <span class="mark-square" aria-hidden="true"></span>
    <span class="wordmark">RW Talbrook LLC</span>
  </section>

  <section class="card card--front" aria-label="Business card front">
    <div class="front-logo">
      <span class="mark-square" aria-hidden="true"></span>
      <span class="wordmark">RW Talbrook LLC</span>
    </div>
    <div class="divider-band" aria-hidden="true"></div>
    <div class="contact-block">
      <p class="person-name">Dale <span class="surname">Morrow</span></p>
      <p class="person-role">ENGINEER</p>
      <div class="rule-pair" aria-hidden="true"><span class="rule-white"></span><span class="rule-orange"></span></div>
      <ul class="contact-list">
        <li class="contact-item">
          <svg class="contact-icon" viewBox="0 0 26 26" fill="none" stroke="var(--brand-blue)" stroke-width="1.6" aria-hidden="true">
            <circle cx="13" cy="13" r="11"/>
            <path d="M9 8c-1 2 1 6 4 8 2 1 3 1 4 0l-2-2-1 1c-1-1-2-2-3-4l1-1-2-2z" stroke-linejoin="round"/>
          </svg>
          <span>+(000) 310.482.615<br>+(000) 527.904.318</span>
        </li>
        <li class="contact-item">
          <svg class="contact-icon" viewBox="0 0 26 26" fill="none" stroke="var(--brand-blue)" stroke-width="1.6" aria-hidden="true">
            <path d="M13 24s-8-8-8-13a8 8 0 0 1 16 0c0 5-8 13-8 13z"/>
            <circle cx="13" cy="11" r="3"/>
          </svg>
          <span>info@rwtalbrook.com<br>www.rwtalbrook.com</span>
        </li>
        <li class="contact-item">
          <svg class="contact-icon" viewBox="0 0 26 26" fill="none" stroke="var(--brand-blue)" stroke-width="1.6" aria-hidden="true">
            <circle cx="13" cy="13" r="11"/>
            <ellipse cx="13" cy="13" rx="5" ry="11"/>
            <path d="M2 13h22M4 7h18M4 19h18"/>
          </svg>
          <span>42, Harlow Street,<br>Brenton, USA.</span>
        </li>
      </ul>
    </div>
  </section>
</body>
</html>
```